Meridane Haulage - Website

A clean, not cluttered informative website for our business. We specialize in the transportation of radioactive materials across North America. The site is mostly for information about our company and will not be used to attract business but will be used to attract employee's mainly drivers. Driver's are very hard to find in our area. One of the pages needs to be a job's posting page with an apply now button. Either an application can be filled out there or a resume can be uploaded which ever functionality works better. I would like a website that I can easily edit, ability to change text and photos.

Number of Pages Required

5+ page

Colors

Designer to choose colors to be used in the design.

Requirements
Must have
• Home - About - Services - Jobs - Contact pages
• A way prospective employee's can apply or upload their resume to be emailed to me
• Very clean apperance
Should not have
• I don't want it to be busy

```html
<!DOCTYPE html>
<html lang="en">
<head>
<meta charset="utf-8">
<title>Meridane Haulage</title>
<link href="https://fonts.googleapis.com/css2?family=Raleway:wght@500;600;700&family=Open+Sans:wght@400;600&display=swap" rel="stylesheet">
<style>
:root{
  --blue:#1474c4;
  --blue-dark:#0d5fa6;
  --ink:#222;
  --text:#555;
  --light:#f7f7f7;
  --white:#fff;
  --line:#dcdcdc;
  --footer:#2b2b2b;
  --head:'Raleway',sans-serif;
  --body:'Open Sans',sans-serif;
}
*{box-sizing:border-box;margin:0;padding:0}
html,body{width:1200px;height:2473px;overflow:hidden}
body{position:relative;background:var(--white);font-family:var(--body);color:var(--text)}
.abs{position:absolute}
.top-strip{left:0;top:0;width:1200px;height:13px;background:linear-gradient(90deg,var(--blue) 0 30%,#3a8fd6 30% 100%)}
.site-header{left:0;top:13px;width:1200px;height:124px;background:var(--light)}
.brand{left:135px;top:55px;font-family:var(--head);font-weight:700;font-size:34px;color:var(--blue);letter-spacing:1px;white-space:nowrap}
.main-nav a{position:absolute;top:68px;font-family:var(--body);font-weight:600;font-size:15px;color:var(--ink);text-decoration:none}
.nav-active{left:537px;top:133px;width:66px;height:3px;background:var(--blue)}
.search-icon{left:1048px;top:66px}
.hero{left:0;top:137px;width:1200px;height:437px;overflow:hidden}
.hero-photo{left:0;top:0;width:1200px;height:437px;background:linear-gradient(180deg,#7fb0e0 0%,#c9dcef 40%,#3d5fa8 60%,#556b55 80%,#6f6f6f 100%)}
.hero-panel{left:0;top:0}
.hero-title{left:132px;top:238px;font-family:var(--head);font-weight:700;font-size:36px;line-height:39px;color:var(--white);letter-spacing:.5px}
.btn-outline{position:absolute;height:41px;border:2px solid var(--white);color:var(--white);font-family:var(--head);font-weight:500;font-size:19px;display:flex;align-items:center;justify-content:center}
.services{left:0;top:574px;width:1200px;height:387px;background:var(--light)}
.section-title{font-family:var(--head);font-weight:600;font-size:23px;color:var(--blue);letter-spacing:1px}
.svc-title{position:absolute;font-family:var(--head);font-weight:500;font-size:19px;color:var(--ink)}
.svc-text{position:absolute;width:230px;font-size:13px;line-height:15.5px;color:var(--text)}
.svc-icon{position:absolute}
.svc-photo{left:793px;top:682px;width:275px;height:229px;background:linear-gradient(180deg,#6fa8e0 0%,#b9d4ef 45%,#e9ecef 60%,#7a7a6e 100%);box-shadow:4px 4px 10px rgba(0,0,0,.25)}
.about-photo{left:0;top:997px;width:593px;height:420px;background:radial-gradient(ellipse at 45% 55%,#f2f2f2 0%,#d9dcdf 45%,rgba(255,255,255,0) 72%)}
.about-text{left:598px;top:1142px;width:465px;font-size:13px;line-height:15.5px;color:var(--text)}
.btn-solid{position:absolute;height:41px;background:var(--blue);color:var(--white);font-family:var(--head);font-weight:500;font-size:19px;display:flex;align-items:center;justify-content:center}
.jobs{left:0;top:1464px;width:1200px;height:451px;background:linear-gradient(180deg,#1e4e79 0%,#2c5f86 45%,#3a6b8c 75%,#4a6f87 100%)}
.jobs-title{left:0;top:1500px;width:1200px;text-align:center;font-family:var(--head);font-weight:600;font-size:23px;color:var(--white);letter-spacing:1px}
.job-title{position:absolute;font-family:var(--head);font-weight:500;font-size:19px;color:var(--white)}
.job-text{position:absolute;width:400px;font-size:13px;line-height:15.5px;color:var(--white)}
.lower{left:0;top:1915px;width:1200px;height:381px;background:var(--light)}
.faq-item{position:absolute;left:132px;width:270px;border:1px solid var(--line);background:var(--white);padding:0 14px}
.faq-q{height:36px;display:flex;align-items:center;justify-content:space-between;font-family:var(--head);font-weight:700;font-size:12px;color:var(--ink)}
.faq-a{font-size:10px;line-height:12px;color:var(--text);padding-bottom:10px}
.news-box{left:463px;top:2011px;width:269px;height:242px;border:1px solid var(--line);background:var(--white)}
.news-date{position:absolute;left:480px;width:65px;background:var(--blue);color:var(--white);font-family:var(--head);font-weight:600;font-size:19px;line-height:22px;text-align:center;display:flex;align-items:center;justify-content:center}
.news-head{position:absolute;left:557px;font-family:var(--head);font-weight:700;font-size:12px;color:var(--ink)}
.news-text{position:absolute;left:557px;width:160px;font-size:9.5px;line-height:12px;color:var(--text)}
.join-text{left:793px;top:2011px;width:275px;font-size:13px;line-height:15.5px;color:var(--text)}
.upload-field{left:793px;top:2100px;width:275px;height:47px;border:1px solid var(--line);background:var(--white);display:flex;align-items:center;justify-content:space-between;padding:0 14px;font-size:12px;color:#999}
.site-footer{left:0;top:2296px;width:1200px;height:177px;background:var(--footer)}
.footer-brand{left:132px;top:2358px;font-family:var(--head);font-weight:700;font-size:28px;color:var(--white);white-space:nowrap}
.footer-copy{left:132px;top:2404px;font-size:9px;color:#bbb}
.footer-head{position:absolute;top:2350px;font-family:var(--head);font-weight:600;font-size:13px;color:var(--white)}
.footer-text{position:absolute;top:2381px;font-size:12px;line-height:17px;color:#ddd}
.footer-rule{position:absolute;top:2345px;width:1px;height:80px;background:#555}
.social{position:absolute;top:2388px;width:20px;height:20px;border:1.5px solid #ddd;border-radius:50%}
</style>
</head>
<body>

<div class="abs top-strip"></div>
<header class="abs site-header"></header>
<div class="abs brand">Meridane Haulage</div>
<nav class="main-nav">
  <a style="left:550px">Home</a>
  <a style="left:639px">Services</a>
  <a style="left:746px">About Us</a>
  <a style="left:855px">Jobs</a>
  <a style="left:928px">Contact Us</a>
</nav>
<div class="abs nav-active"></div>
<svg class="abs search-icon" width="22" height="22" viewBox="0 0 22 22"><circle cx="9" cy="9" r="7" fill="none" stroke="#222" stroke-width="2"/><line x1="14" y1="14" x2="20" y2="20" stroke="#222" stroke-width="2"/></svg>

<section class="abs hero">
  <div class="abs hero-photo" role="img" aria-label="Blue articulated truck driving along a coastal highway under a cloudy sky"></div>
  <svg class="abs hero-panel" width="1200" height="437" viewBox="0 0 1200 437"><polygon points="0,0 437,0 676,437 0,437" fill="#1474c4"/></svg>
</section>
<h1 class="abs hero-title">STRONGEST<br>DISTRIBUTION<br>NETWORK</h1>
<a class="btn-outline" style="left:132px;top:387px;width:160px">Read More</a>
<a class="btn-outline" style="left:311px;top:387px;width:160px">Apply for Job</a>

<section class="abs services"></section>
<h2 class="abs section-title" style="left:0;top:616px;width:1200px;text-align:center">OUR SERVICES</h2>
<svg class="svc-icon" style="left:133px;top:684px" width="28" height="28" viewBox="0 0 28 28"><circle cx="14" cy="14" r="12" fill="#333"/><path d="M8 8c3 1 4 4 3 6s2 4 1 7M16 5c0 3 4 3 5 6s-2 4 0 7" stroke="#fff" stroke-width="1.6" fill="none"/></svg>
<div class="svc-title" style="left:186px;top:678px">Lorem ipsum dolor sit</div>
<p class="svc-text" style="left:186px;top:714px">quia quam aliquet. Dolor laoreet vitae aenean vulputate ut feugiat, pharetra quis vivamus, eleifend faucibus</p>
<svg class="svc-icon" style="left:462px;top:684px" width="38" height="24" viewBox="0 0 38 24"><rect x="0" y="2" width="24" height="15" fill="#333"/><path d="M25 7h7l5 6v4H25z" fill="#333"/><circle cx="7" cy="20" r="3.5" fill="#333"/><circle cx="30" cy="20" r="3.5" fill="#333"/></svg>
<div class="svc-title" style="left:516px;top:678px">Lorem ipsum dolor sit</div>
<p class="svc-text" style="left:516px;top:714px">quia quam aliquet. Dolor laoreet vitae aenean vulputate ut feugiat, pharetra quis vivamus, eleifend faucibus</p>
<svg class="svc-icon" style="left:133px;top:806px" width="20" height="36" viewBox="0 0 20 36"><text x="10" y="30" text-anchor="middle" font-family="Open Sans,sans-serif" font-weight="700" font-size="34" fill="#333">$</text></svg>
<div class="svc-title" style="left:186px;top:804px">Lorem ipsum dolor sit</div>
<p class="svc-text" style="left:186px;top:840px">quia quam aliquet. Dolor laoreet vitae aenean vulputate ut feugiat, pharetra quis vivamus, eleifend faucibus</p>
<svg class="svc-icon" style="left:463px;top:808px" width="32" height="32" viewBox="0 0 32 32"><circle cx="16" cy="16" r="10" fill="none" stroke="#333" stroke-width="6" stroke-dasharray="4 3"/><circle cx="16" cy="16" r="8" fill="#333"/><circle cx="16" cy="16" r="3.5" fill="#f7f7f7"/></svg>
<div class="svc-title" style="left:516px;top:804px">Lorem ipsum dolor sit</div>
<p class="svc-text" style="left:516px;top:840px">quia quam aliquet. Dolor laoreet vitae aenean vulputate ut feugiat, pharetra quis vivamus, eleifend faucibus</p>
<div class="abs svc-photo" role="img" aria-label="Driver standing beside a white semi truck"></div>

<div class="abs about-photo" role="img" aria-label="White semi truck with trailer on a white backdrop"></div>
<h2 class="abs section-title" style="left:598px;top:1082px">ABOUT US</h2>
<p class="abs about-text">Lorem ipsum dolor sit amet, egestas at ornare integer ullamcorper, vel eu aliquam integer varius imperdiet, felis rhoncus, nulla congue et vel wisi mi in, sociis orci integer turpis purus non. Sapien bibendum fermentum non vivamus. Lectus tempus enim, dolores nunc. Lacinia dapibus, mi eget ultrices. Etiam erat aliquam sodales quis, dignissim sollicitudin nec, nisl eu orci a vitae sed lacus. Curabitur velit donec varius imperdiet amet metus, ut vestibulum, maecenas erat.</p>
<a class="btn-solid" style="left:598px;top:1289px;width:160px">Read More</a>

<section class="abs jobs" role="img" aria-label="Truck on a mountain highway with forest, tinted blue"></section>
<h2 class="abs jobs-title">JOBS &amp; CAREERS</h2>
<div class="job-title" style="left:132px;top:1556px">Lorem ipsum dolor sit</div>
<p class="job-text" style="left:132px;top:1589px">quia quam aliquet. Dolor laoreet vitae aenean vulputate ut feugiat, pharetra quis vivamus, eleifend faucibus, quia quam aliquet.</p>
<a class="btn-outline" style="left:132px;top:1648px;width:160px">Apply Now</a>
<div class="job-title" style="left:598px;top:1556px">Lorem ipsum dolor sit</div>
<p class="job-text" style="left:598px;top:1589px">quia quam aliquet. Dolor laoreet vitae aenean vulputate ut feugiat, pharetra quis vivamus, eleifend faucibus</p>
<a class="btn-outline" style="left:598px;top:1648px;width:160px">Apply Now</a>
<div class="job-title" style="left:132px;top:1740px">Lorem ipsum dolor sit</div>
<p class="job-text" style="left:132px;top:1773px">quia quam aliquet. Dolor laoreet vitae aenean vulputate ut feugiat, pharetra quis vivamus, eleifend faucibus</p>
<a class="btn-outline" style="left:132px;top:1833px;width:160px">Apply Now</a>
<div class="job-title" style="left:601px;top:1735px">Lorem ipsum dolor sit</div>
<p class="job-text" style="left:601px;top:1768px">quia quam aliquet. Dolor laoreet vitae aenean vulputate ut feugiat, pharetra quis vivamus, eleifend faucibus</p>
<a class="btn-outline" style="left:601px;top:1827px;width:160px">Apply Now</a>

<section class="abs lower"></section>
<h2 class="abs section-title" style="left:132px;top:1953px">FAQs</h2>
<h2 class="abs section-title" style="left:463px;top:1953px">NEWS</h2>
<h2 class="abs section-title" style="left:791px;top:1953px">JOIN OUR TEAM</h2>

<div class="faq-item" style="top:2011px"><div class="faq-q">Lorem ipsum dolor sit amet<svg width="14" height="8" viewBox="0 0 14 8"><path d="M1 1l6 6 6-6" stroke="#333" stroke-width="1.5" fill="none"/></svg></div></div>
<div class="faq-item" style="top:2065px"><div class="faq-q">Lorem ipsum dolor sit amet<svg width="14" height="8" viewBox="0 0 14 8"><path d="M1 7l6-6 6 6" stroke="#333" stroke-width="1.5" fill="none"/></svg></div>
<p class="faq-a">Lorem ipsum dolor sit amet, consectetur adipiscing elit, sed do eiusmod tempor incididunt ut labore et dolore magna aliqua. Lorem ipsum dolor sit amet, consectetur adipiscing elit, sed do eiusmod tempor incididunt ut labore et dolore magna aliqua.</p></div>
<div class="faq-item" style="top:2217px"><div class="faq-q">Lorem ipsum dolor sit amet<svg width="14" height="8" viewBox="0 0 14 8"><path d="M1 1l6 6 6-6" stroke="#333" stroke-width="1.5" fill="none"/></svg></div></div>

<div class="abs news-box"></div>
<div class="news-date" style="top:2029px;height:97px">03<br>Mar</div>
<div class="news-head" style="top:2050px">Lorem ipsum dolor sit</div>
<p class="news-text" style="top:2080px">Lorem ipsum dolor sit amet, consectetur adipiscing elit, sed do</p>
<div class="news-date" style="top:2137px;height:96px">08<br>Dec</div>
<div class="news-head" style="top:2152px">Lorem ipsum dolor sit</div>
<p class="news-text" style="top:2182px">Lorem ipsum dolor sit amet, consectetur adipiscing elit, sed do</p>

<p class="abs join-text">Lorem ipsum dolor sit amet, consectetur adipiscing elit, sed do eiusmod tempor incididunt ut labore et dolore magna aliqua.</p>
<div class="abs upload-field">Upload Your Resume<svg width="16" height="16" viewBox="0 0 16 16"><circle cx="8" cy="8" r="7" fill="none" stroke="#222" stroke-width="1.5"/><path d="M8 12V5M5 8l3-3 3 3" stroke="#222" stroke-width="1.5" fill="none"/></svg></div>
<a class="btn-solid" style="left:910px;top:2175px;width:160px">Send</a>

<footer class="abs site-footer"></footer>
<div class="abs footer-brand">Meridane Haulage</div>
<div class="abs footer-copy">All Rights Reserved © 2019 Meridane Haulage</div>
<div class="footer-rule" style="left:409px"></div>
<div class="footer-rule" style="left:664px"></div>
<div class="footer-rule" style="left:901px"></div>
<div class="footer-head" style="left:452px">SHOWROOM</div>
<p class="footer-text" style="left:452px">48 Alder Row<br>Brookvale, Ohio 43012</p>
<div class="footer-head" style="left:704px">TOLL FREE NUMBER</div>
<p class="footer-text" style="left:704px">Office: 555 014 2290<br>Fax: 555 014 2291</p>
<div class="footer-head" style="left:949px">FOLLOW US</div>
<span class="social" style="left:950px"></span>
<span class="social" style="left:976px"></span>
<span class="social" style="left:1002px"></span>
<span class="social" style="left:1028px"></span>

</body>
</html>
```